Business cards for start-up accounting firm

I'm looking for a double sided business card ready for upload into Lumo print or similar print providers with no modification required by me.
I'm looking for something simple as i think cards that are too 'busy' actually detract from the message. I have some thoughts but more than happy to see what comes up. The logo i have came out of left field and i love it the moment i saw it!

My thoughts:

Side 1: Just the logo, perhaps on a dark grey or charcoal background to make the logo colours stand out?

Side 2: The call to action from me website 'Looking for a more relaxed, friendly and interactive relationship with your accountant?' with my contact information
Name: Gus Tarrow
Email: gus@ledgerowl.com.au
Website: www.ledgerowl.com.au
Phone: 1300 762 349

The call to action needs to be the first thing they see when they look at side 2. If it helps to know what we do and how we do it there is a draft website at www.ledgerowl.com.au

Like i said, happy to consider anything that comes up :)

Target Market(s)

i'm targeting small business owners who experience a lot of stress around finacial reporting and have had bad experiences with accountants in the past.

Industry/Entity Type

Accounting

Contact Information for Business Card

Contained in the Description

Font styles to use
Serif
Sans Serif
Other font styles liked:
• See logo files attached

Colors
474747

Requirements
Must have
• My logo, slogan and contact information

```html
<!DOCTYPE html>
<html lang="en">
<head>
<meta charset="utf-8">
<title>Ledger Owl – Business Cards</title>
<link rel="stylesheet" href="https://fonts.googleapis.com/css2?family=Roboto:wght@400;700;900&display=swap">
<style>
  :root {
    --page: #ece8e2;
    --violet: #b847bf;
    --violet-light: #cb68d1;
    --violet-text: #c85fce;
    --charcoal: #2f2f30;
    --charcoal-light: #474747;
    --yellow: #f2e332;
    --soft-grey: #c9c9c9;
    --card-w: 540px;
    --card-h: 309px;
  }
  * { box-sizing: border-box; margin: 0; padding: 0; }
  html, body {
    width: 1200px; height: 1023px; overflow: hidden;
    background: var(--page);
    font-family: "Roboto", Arial, sans-serif;
  }
  .card-sheet {
    position: relative; width: 1200px; height: 1023px;
    display: flex; justify-content: center; align-items: center; gap: 40px;
  }
  .card {
    position: relative; width: var(--card-w); height: var(--card-h);
    border-radius: 4px; overflow: hidden;
    box-shadow: 0 10px 28px rgba(0,0,0,.22);
  }

  /* Side 2: call to action */
  .card--contact { background: linear-gradient(160deg, var(--violet-light), var(--violet) 60%); }
  .card__swoosh { position: absolute; inset: 0; }
  .call-to-action {
    position: absolute; left: 24px; top: 118px; width: 420px;
    color: var(--yellow); font-weight: 700; font-size: 17px; line-height: 1.5;
    text-align: center;
  }
  .holder-name {
    position: absolute; right: 120px; top: 214px;
    color: var(--violet-text); font-weight: 700; font-size: 19px; letter-spacing: .5px;
    text-transform: uppercase;
  }
  .contact-row {
    position: absolute; left: 22px; right: 18px; bottom: 22px;
    display: flex; justify-content: space-between;
    list-style: none; color: var(--soft-grey); font-size: 13px;
  }
  .contact-row li { display: flex; align-items: center; gap: 6px; }
  .contact-row svg { width: 14px; height: 14px; }

  /* Side 1: brand */
  .card--brand {
    background: linear-gradient(150deg, var(--charcoal-light), var(--charcoal) 55%);
    display: flex; align-items: center; justify-content: center;
  }
  .brand-name {
    color: var(--yellow); font-weight: 900; font-size: 46px; letter-spacing: 1px;
    text-transform: uppercase;
  }
</style>
</head>
<body>
<main class="card-sheet">
  <section class="card card--contact" aria-label="Contact side">
    <svg class="card__swoosh" viewBox="0 0 540 309" preserveAspectRatio="none" aria-hidden="true">
      <path d="M0,309 L0,262 C150,262 400,232 540,58 L540,309 Z" fill="var(--charcoal)"/>
      <path d="M20,258 C180,250 420,210 510,95 C440,190 300,245 20,258 Z" fill="var(--charcoal-light)" opacity=".6"/>
    </svg>
    <p class="call-to-action">Looking for a more relaxed, friendly<br>and interactive relationship with your accountant?</p>
    <h2 class="holder-name">Gus Tarrow</h2>
    <ul class="contact-row">
      <li>
        <svg viewBox="0 0 14 14"><circle cx="7" cy="7" r="7" fill="var(--violet-text)"/><path d="M4.5,3.5 L6,3.5 L6.6,5.4 L5.7,6.1 Q6.5,7.8 7.9,8.4 L8.6,7.5 L10.5,8.1 L10.5,9.6 Q6,10.2 4.5,3.5 Z" fill="var(--charcoal)"/></svg>
        1300 762 349
      </li>
      <li>
        <svg viewBox="0 0 14 14"><circle cx="7" cy="7" r="7" fill="var(--violet-text)"/><rect x="3.5" y="4.5" width="7" height="5" fill="var(--charcoal)"/><path d="M3.5,4.5 L7,7.3 L10.5,4.5" stroke="var(--violet-text)" fill="none" stroke-width=".8"/></svg>
        gus@ledgerowl.com.au
      </li>
      <li>
        <svg viewBox="0 0 14 14"><circle cx="7" cy="7" r="7" fill="var(--violet-text)"/><circle cx="7" cy="7" r="3.8" fill="none" stroke="var(--charcoal)" stroke-width=".9"/><path d="M3.2,7 H10.8 M7,3.2 V10.8" stroke="var(--charcoal)" stroke-width=".9"/></svg>
        www.ledgerowl.com.au
      </li>
    </ul>
  </section>

  <section class="card card--brand" aria-label="Brand side">
    <h1 class="brand-name">Ledger Owl</h1>
  </section>
</main>
</body>
</html>
```